Meadowlark Suds Business Card

The new business card design will incorporate my new logo components designed by one of your designers. Meadowlark Suds creates high quality soaps and bath products. They would be suited for a Spa, Bed and Breakfast, Boutique environment. The look should be a white background.
Classy, soft and using the colour palet of the logo. The card will be two sided.
Updates

Target Market(s)

Looking to appeal to an upper end market. Spas, boutiques, independent gift stores, bridal salons, bed and breakfast, etc. I want the card to impart a sense of elegance, tranquility and Meadowlark. But also quality and value.

Industry/Entity Type

Business

Font styles to use
Sans Serif
Script

Requirements
Must have
• My logo on the front. But also on the back but faded out to allow written notes on the back.
On the front : Carla Penwick
Owner/Creator
47 Ashgrove Rd
Guelph, Ont K4R 2P9
613.402.9186
Creating Quality Handcrafted Soaps And Bath Products
Custom and Wholesale Orders Welcome
Www.meadowlarksuds-example.ca
Www.facebook.com / MeadowlarkSudsandTub
info@meadowlarksuds-example.ca

```html
<!DOCTYPE html>
<html lang="en">
<head>
<meta charset="utf-8">
<title>Meadowlark Suds Business Card</title>
<link href="https://fonts.googleapis.com/css2?family=Saira:wght@300;400;500&display=swap" rel="stylesheet">
<style>
  :root {
    --page: #e9e8e6;
    --card: #ffffff;
    --ink: #2f3133;
    --ink-soft: #55585b;
    --sage: #86b3a8;
    --sage-deep: #6e9e93;
    --silver: #c9c9c9;
  }
  * { margin: 0; padding: 0; box-sizing: border-box; }
  html, body { width: 1200px; height: 900px; overflow: hidden; background: var(--page); }
  body { font-family: "Saira", Arial, sans-serif; color: var(--ink); }
  .business-card {
    position: absolute; left: 180px; top: 210px;
    width: 840px; height: 480px;
    background: var(--card); border-radius: 36px; overflow: hidden;
    box-shadow: 0 10px 30px rgba(0,0,0,.12);
  }
  .card-waves { position: absolute; inset: 0; }
  .wave-url { font-family: "Saira", Arial, sans-serif; font-size: 18px; letter-spacing: 5px; fill: #fff; }
  .brand {
    position: absolute; left: 80px; top: 196px;
    display: flex; align-items: center; gap: 16px;
  }
  .brand-dot { width: 54px; height: 54px; border-radius: 50%; background: var(--sage); opacity: .75; }
  .brand-name { font-size: 34px; font-weight: 400; color: var(--sage-deep); letter-spacing: .5px; white-space: nowrap; }
  .contact { position: absolute; left: 510px; top: 44px; width: 320px; white-space: nowrap; }
  .contact-name { font-size: 21px; font-weight: 500; letter-spacing: 1.5px; text-transform: uppercase; line-height: 30px; }
  .contact-role { font-size: 18px; color: var(--ink-soft); line-height: 27px; }
  .contact-address { font-size: 16px; color: var(--ink-soft); margin-top: 22px; line-height: 1.35; padding-left: 30px; }
  .contact-list { list-style: none; margin-top: 22px; padding-left: 50px; }
  .contact-list li { display: flex; align-items: center; gap: 10px; font-size: 14px; font-weight: 300; line-height: 24px; }
  .contact-list svg { width: 14px; height: 14px; fill: var(--ink); flex: none; }
</style>
</head>
<body>
<div class="business-card">
  <svg class="card-waves" width="840" height="480" viewBox="0 0 840 480">
    <path d="M0,452 Q430,430 840,372 L840,480 L0,480Z" fill="var(--silver)"/>
    <path d="M0,468 Q430,446 840,388 L840,480 L0,480Z" fill="var(--sage)"/>
    <path id="url-line" d="M240,466 Q520,444 780,404" fill="none"/>
    <text class="wave-url"><textPath href="#url-line">www.meadowlarksuds-example.ca</textPath></text>
  </svg>

  <div class="brand">
    <span class="brand-dot"></span>
    <span class="brand-name">Meadowlark Suds</span>
  </div>

  <div class="contact">
    <p class="contact-name">Owen Hartfield</p>
    <p class="contact-role">Owner/Creator</p>
    <p class="contact-address">47 Ashgrove Rd<br>Guelph, Ont K4R 2P9</p>
    <ul class="contact-list">
      <li><svg viewBox="0 0 16 16"><path d="M3 1l3 3-2 2c1 2 3 4 5 5l2-2 3 3-2 3C6 14 2 10 1 4z"/></svg>613.402.9186</li>
      <li><svg viewBox="0 0 16 16"><path d="M4 0h8v16H4zM5 2v10h6V2zm3 11a1 1 0 100 2 1 1 0 000-2z"/></svg>613.402.9186</li>
      <li><svg viewBox="0 0 16 16"><path d="M4 1h7v4H4zM1 6h14v9H1zm3 2v2h2V8zm4 0v2h2V8z"/></svg>613.402.9186</li>
      <li><svg viewBox="0 0 16 16"><path d="M0 3h16v10H0zm1 1v1l7 4 7-4V4z"/></svg>info@meadowlarksuds-example.ca</li>
      <li><svg viewBox="0 0 16 16"><path d="M8 0a8 8 0 100 16A8 8 0 008 0zm-1 2v3H4c.6-1.5 1.7-2.6 3-3zm2 0c1.3.4 2.4 1.5 3 3H9zM2.3 7H7v2H2.3zM9 7h4.7v2H9zM4 11h3v3c-1.3-.4-2.4-1.5-3-3zm5 0h3c-.6 1.5-1.7 2.6-3 3z"/></svg>www.meadowlarksuds-example.ca</li>
    </ul>
  </div>
</div>
</body>
</html>
```